Corvallina
Logo ai and eps files uploaded.
Thanks
please upload the logo ai file or eps
Designers, already looking great. Please include letter head and envelope. Also, the business card is a folded card.
Thanks for participating.
Greta
Logo????
Logo?

```html
<!DOCTYPE html>
<html lang="en">
<head>
<meta charset="utf-8">
<title>Corvallina Stationery</title>
<link rel="stylesheet" href="https://fonts.googleapis.com/css2?family=Raleway:wght@400;500&display=swap">
<style>
:root{
  --purple:#5a2d82;
  --ink:#555555;
  --ink-soft:#8a8a8a;
  --paper:#ffffff;
  --edge:#d9d9d9;
  --bg:#ffffff;
  --tint:#ece6f2;
  --tint-soft:#f6f3f9;
}
*{margin:0;padding:0;box-sizing:border-box}
html,body{width:1200px;height:811px;overflow:hidden;background:var(--bg)}
body{position:relative;font-family:"Raleway",sans-serif;color:var(--ink)}
.sheet{position:absolute;background:var(--paper);border:1px solid var(--edge);overflow:hidden}

/* wordmark stand-in */
.wordmark{position:absolute;left:0;right:0;text-align:center;color:var(--purple);line-height:1.1}
.wordmark .name{display:inline-flex;align-items:center;gap:.35em;font-weight:500;letter-spacing:.02em}
.wordmark .dot{display:inline-block;width:.5em;height:.5em;border-radius:50%;background:var(--purple)}
.wordmark .owner{display:block;font-weight:400;letter-spacing:.12em;text-transform:uppercase;color:var(--purple)}

/* business cards */
.card{width:216px;height:120px}
.card-front{left:96px;top:60px}
.card-inside{left:329px;top:60px}
.card-back{left:96px;top:199px;background:var(--purple);border-color:var(--purple)}
.card-products{left:329px;top:199px}
.card-front .person{position:absolute;top:14px;left:0;right:0;text-align:center;font-size:7px;color:var(--ink)}
.card-front .person small{display:block;font-size:5px;color:var(--ink-soft);margin-top:2px}
.card-front .wordmark{top:46px;font-size:17px}
.card-front .wordmark .owner{font-size:6px;margin-top:3px}
.card-inside .wordmark{top:24px;font-size:17px}
.card-inside .wordmark .owner{font-size:6px;margin-top:3px}
.card-inside .contact{position:absolute;top:68px;left:0;right:0;text-align:center;font-size:5px;line-height:1.6;color:var(--ink-soft)}
.card-back .wordmark{top:52px;font-size:14px;color:var(--paper)}
.card-back .wordmark .dot{background:var(--paper)}
.card-products .label{position:absolute;top:16px;left:0;right:0;text-align:center;font-size:6px;letter-spacing:.3em;color:var(--ink-soft)}
.card-products .product-art{position:absolute;left:68px;top:36px;width:80px;height:64px;background:radial-gradient(ellipse at center,var(--tint) 0%,var(--tint-soft) 70%,var(--paper) 100%)}

/* envelope */
.envelope{left:29px;top:461px;width:595px;height:326px}
.envelope .flap{position:absolute;left:0;top:0;width:595px;height:100px}
.envelope .wordmark{top:110px;font-size:30px}
.envelope .wordmark .owner{font-size:9px;margin-top:4px}
.envelope .return{position:absolute;left:0;right:0;top:298px;text-align:center;font-size:7px;letter-spacing:.04em;color:var(--ink-soft)}

/* letterhead */
.letterhead{left:636px;top:29px;width:535px;height:758px}
.letterhead .wordmark{top:34px;font-size:30px}
.letterhead .wordmark .owner{font-size:9px;margin-top:4px}
.letterhead .footer-text{position:absolute;left:0;right:0;bottom:30px;text-align:center;font-size:7px;letter-spacing:.03em;color:var(--ink-soft)}
.letterhead .footer-text .web{color:var(--purple)}
.letterhead .footer-band{position:absolute;left:0;right:0;bottom:6px;height:9px;background:var(--purple)}

.faint-art{position:absolute;background:radial-gradient(ellipse at center,var(--tint-soft) 0%,rgba(246,243,249,0) 70%)}
.envelope .faint-art{left:390px;top:130px;width:180px;height:170px}
.letterhead .faint-art{left:130px;top:260px;width:280px;height:260px}
</style>
</head>
<body>

<section class="sheet card card-front" aria-label="Business card front">
  <p class="person">Greta Marlowe<small>Owner</small></p>
  <div class="wordmark"><span class="name"><span class="dot"></span>Corvallina</span><span class="owner">Greta Marlowe</span></div>
</section>

<section class="sheet card card-inside" aria-label="Business card inside">
  <div class="wordmark"><span class="name"><span class="dot"></span>Corvallina</span><span class="owner">Greta Marlowe</span></div>
  <p class="contact">88 Linden Hollow Road, Fairmont, CA 90210<br>P 555 010 2200 &nbsp;E greta@corvallina.com<br>corvallina.com</p>
</section>

<section class="sheet card card-back" aria-label="Business card back">
  <div class="wordmark"><span class="name"><span class="dot"></span>Corvallina</span></div>
</section>

<section class="sheet card card-products" aria-label="Business card products panel">
  <p class="label">OUR PRODUCTS</p>
  <div class="product-art" role="img" aria-label="Product imagery area"></div>
</section>

<section class="sheet envelope" aria-label="Envelope">
  <svg class="flap" viewBox="0 0 595 100" aria-hidden="true">
    <path d="M0 0H595V14L297.5 96L0 14Z" fill="var(--purple)"/>
  </svg>
  <div class="wordmark"><span class="name"><span class="dot"></span>Corvallina</span><span class="owner">Greta Marlowe</span></div>
  <div class="faint-art" role="img" aria-label="Faint background brand decoration"></div>
  <p class="return">88 Linden Hollow Road Fairmont, CA 90210</p>
</section>

<section class="sheet letterhead" aria-label="Letterhead">
  <div class="wordmark"><span class="name"><span class="dot"></span>Corvallina</span><span class="owner">Greta Marlowe</span></div>
  <div class="faint-art" role="img" aria-label="Faint background brand decoration"></div>
  <p class="footer-text">88 Linden Hollow Road Fairmont, CA 90210 &nbsp;P 555 010 2200 &nbsp;E greta@corvallina.com &nbsp;<span class="web">corvallina.com</span></p>
  <div class="footer-band"></div>
</section>

</body>
</html>
```